Brell Stone Company Business Cards

Front and Back Business Card - logo and text setup - cool design. I need workable photoshop or illustrator files so I can setup each employee card with design that is created
Updates

Hi everyone, thank you for the great entries. Please no more white and blue cards - there are so many already - black and silver only now please. thanks!

Target Market(s)

Construction Industry - Facility Managers

Industry/Entity Type

Construction

Contact Information for Business Card

I really like contemporary simplistic looks - clean neat....not opposed to seeing some black backrounds

Requirements
Must have
• Logo/website address with design on front only - www.brellstone-example.com (logo attached)
• Back:
• Name/Title/Company Address/Phone/email address
Nice to have
• Cool design
Should not have
• Nothing gimmicky like Fire or Water - since we are a Fire Protection company - it has all been done

```html
<!DOCTYPE html>
<html lang="en">
<head>
<meta charset="utf-8">
<title>Brell Stone Company – Business Cards</title>
<link href="https://fonts.googleapis.com/css2?family=Open+Sans:wght@400;600;700;800&display=swap" rel="stylesheet">
<style>
  :root {
    --backdrop: #1c1c1e;
    --card: #000000;
    --ink: #ffffff;
    --ink-soft: #e6e6e6;
    --accent-red: #ff2424;
    --accent-blue: #1a2ea8;
  }
  * { box-sizing: border-box; margin: 0; padding: 0; }
  html, body {
    width: 1200px;
    height: 960px;
    overflow: hidden;
    background: var(--backdrop);
    font-family: "Open Sans", Arial, sans-serif;
  }
  .sheet {
    width: 1200px;
    height: 960px;
    display: flex;
    flex-direction: column;
    align-items: center;
    justify-content: center;
    gap: 60px;
  }
  .card {
    position: relative;
    width: 700px;
    height: 400px;
    background: var(--card);
    overflow: hidden;
    box-shadow: 0 10px 30px rgba(0,0,0,.45);
  }

  /* Front */
  .card-front .brand {
    position: absolute;
    left: 0; right: 0; top: 150px;
    text-align: center;
  }
  .wordmark {
    color: var(--accent-red);
    font-weight: 800;
    font-size: 50px;
    letter-spacing: -1px;
    line-height: 1;
  }
  .card-front .website {
    margin-top: 34px;
    color: var(--ink-soft);
    font-size: 17px;
    letter-spacing: 4px;
  }

  /* Back */
  .name-tab {
    position: absolute;
    left: 0; top: 28px;
    width: 14px; height: 62px;
    background: var(--accent-red);
    border-radius: 0 14px 14px 0;
  }
  .identity {
    position: absolute;
    left: 34px; top: 32px;
    color: var(--ink);
  }
  .identity .person { font-weight: 700; font-size: 20px; line-height: 1.2; }
  .identity .role { font-size: 18px; line-height: 1.3; }

  .contacts {
    position: absolute;
    left: 34px; top: 140px;
    color: var(--ink);
    font-size: 17px;
    line-height: 1.6;
    list-style: none;
  }
  .contacts li { display: flex; align-items: center; gap: 10px; }
  .contacts svg { width: 16px; height: 16px; flex: none; }
  .address {
    position: absolute;
    left: 34px; top: 230px;
    color: var(--ink);
    font-size: 17px;
    line-height: 1.45;
    font-style: normal;
  }
  .card-back .brand {
    position: absolute;
    right: 50px; top: 100px;
    width: 250px;
    text-align: right;
  }
  .card-back .wordmark {
    font-size: 40px;
    line-height: 1.1;
  }

  .web-tab {
    position: absolute;
    right: 40px; bottom: 0;
    width: 380px; height: 52px;
    background: var(--accent-blue);
    border-radius: 22px 22px 0 0;
    color: var(--ink);
    font-size: 16px;
    letter-spacing: 3px;
    display: flex;
    align-items: center;
    justify-content: center;
  }
</style>
</head>
<body>
<main class="sheet">

  <section class="card card-front" aria-label="Card front">
    <div class="brand">
      <div class="wordmark">Brell Stone Company</div>
      <div class="website">www.brellstone-example.com</div>
    </div>
  </section>

  <section class="card card-back" aria-label="Card back">
    <span class="name-tab"></span>
    <div class="identity">
      <div class="person">Dana Morrow</div>
      <div class="role">President</div>
    </div>

    <ul class="contacts">
      <li>
        <svg viewBox="0 0 16 16" aria-hidden="true"><path fill="var(--accent-red)" d="M4 1l2.5 3-1.5 1.8c.8 1.9 2.3 3.4 4.2 4.2L11 8.5 14 11l-1.5 3C7 14 2 9 2 2.5z"/></svg>
        (555) 014-2287
      </li>
      <li>
        <svg viewBox="0 0 16 16" aria-hidden="true"><rect x="1" y="3" width="14" height="10" fill="var(--accent-red)"/><path d="M1 3l7 6 7-6" fill="none" stroke="#000" stroke-width="1.3"/></svg>
        info@brellstone-example.com
      </li>
    </ul>

    <address class="address">48 Harbor Works Lane<br>Millbrook, NY 10999</address>

    <div class="brand">
      <div class="wordmark">Brell Stone<br>Company</div>
    </div>

    <div class="web-tab">www.brellstone-example.com</div>
  </section>

</main>
</body>
</html>
```